" Consultora em investimentos nos EUA através de aplicações financeiras com resgate do capital após determinado período de tempo. Está incluído no projeto de investimento um seguro de vida internacional que proporciona segurança para si próprio e para sua família. Ou seja nosso cliente investe em dólares em determinado tempo onde durante o período esta coberto por um seguro de vida. No final do período não utilizando o seguro tudo aquilo que investiu retorna ao cliente capitalizado. "

```html
<!DOCTYPE html>
<html lang="pt-BR">
<head>
<meta charset="utf-8">
<title>Harborline — Cartão de Visita</title>
<link href="https://fonts.googleapis.com/css2?family=Montserrat:wght@300;400;500;600&display=swap" rel="stylesheet">
<style>
  :root{
    --backdrop:#e4e4e6;
    --navy:#1d2030;
    --navy-deep:#161826;
    --navy-pattern:#23273a;
    --gold:#c9a24b;
    --gold-light:#ecd58f;
    --white:#f4f4f6;
    --muted:#9a9cab;
  }
  *{box-sizing:border-box;margin:0;padding:0}
  html,body{width:1200px;height:1200px;overflow:hidden}
  body{
    background:var(--backdrop);
    font-family:'Montserrat',sans-serif;
    display:flex;flex-direction:column;align-items:center;justify-content:center;gap:40px;
  }
  .card{
    position:relative;width:960px;height:530px;
    background:linear-gradient(135deg,var(--navy) 0%,var(--navy-deep) 100%);
    box-shadow:0 10px 30px rgba(0,0,0,.18);
    overflow:hidden;
  }
  .card::after{
    content:"";position:absolute;left:0;right:0;bottom:0;height:12px;
    background:linear-gradient(90deg,var(--gold) 0%,var(--gold-light) 50%,var(--gold) 100%);
  }
  .brand{display:flex;flex-direction:column;align-items:center;gap:14px}
  .brand-row{display:flex;align-items:center;gap:22px}
  .brand-square{width:46px;height:46px;background:var(--gold)}
  .brand-name{
    font-weight:300;font-size:54px;letter-spacing:14px;color:var(--white);
    text-transform:uppercase;
  }
  .brand-tagline{
    font-weight:400;font-size:13px;letter-spacing:5px;color:var(--muted);text-transform:uppercase;
  }
  /* front */
  .card--front{display:flex;align-items:center;justify-content:center}
  /* back */
  .card--back{display:flex}
  .back-brand{
    position:relative;width:50%;height:100%;
    display:flex;align-items:center;justify-content:center;
  }
  .back-brand .pattern-fill{
    position:absolute;inset:0;
    background:linear-gradient(135deg,var(--navy-pattern),var(--navy-deep));
  }
  .back-brand .brand{position:relative}
  .back-brand .brand-name{font-size:38px;letter-spacing:9px}
  .back-brand .brand-square{width:34px;height:34px}
  .back-brand .brand-tagline{font-size:10px;letter-spacing:4px}
  .divider{width:1px;background:var(--gold);margin:70px 0}
  .contact{
    flex:1;padding:80px 0 0 56px;color:var(--white);
  }
  .contact-name{font-weight:500;font-size:30px;letter-spacing:1px}
  .contact-role{font-weight:300;font-size:16px;color:var(--muted);margin:6px 0 34px}
  .contact-list{list-style:none;display:flex;flex-direction:column;gap:16px}
  .contact-item{display:flex;align-items:center;gap:16px;font-size:16px;font-weight:300}
  .contact-item svg{width:20px;height:20px;flex:none}
</style>
</head>
<body>

<section class="card card--front">
  <div class="brand">
    <div class="brand-row">
      <span class="brand-square"></span>
      <span class="brand-name">Harborline</span>
    </div>
    <span class="brand-tagline">Consultoria em Investimentos</span>
  </div>
</section>

<section class="card card--back">
  <div class="back-brand">
    <div class="pattern-fill" role="img" aria-label="Padrão geométrico decorativo em tons de azul-marinho"></div>
    <div class="brand">
      <div class="brand-row">
        <span class="brand-square"></span>
        <span class="brand-name">Harborline</span>
      </div>
      <span class="brand-tagline">Consultoria em Investimentos</span>
    </div>
  </div>
  <div class="divider"></div>
  <div class="contact">
    <p class="contact-name">Nome Sobrenome</p>
    <p class="contact-role">Cargo</p>
    <ul class="contact-list">
      <li class="contact-item">
        <svg viewBox="0 0 24 24" fill="none" stroke="var(--gold)" stroke-width="2"><path d="M5 3h4l2 5-2.5 1.5a11 11 0 0 0 6 6L16 13l5 2v4a2 2 0 0 1-2 2A16 16 0 0 1 3 5a2 2 0 0 1 2-2z"/></svg>
        +55 11 9999 8888
      </li>
      <li class="contact-item">
        <svg viewBox="0 0 24 24" fill="none" stroke="var(--gold)" stroke-width="2"><rect x="6" y="2" width="12" height="20" rx="2"/><line x1="11" y1="18" x2="13" y2="18"/></svg>
        +55 11 9999 7777
      </li>
      <li class="contact-item">
        <svg viewBox="0 0 24 24" fill="none" stroke="var(--gold)" stroke-width="2"><rect x="3" y="5" width="18" height="14" rx="1"/><path d="M3 6l9 7 9-7"/></svg>
        contato@harborline.com.br
      </li>
      <li class="contact-item">
        <svg viewBox="0 0 24 24" fill="none" stroke="var(--gold)" stroke-width="2"><circle cx="12" cy="12" r="9"/><path d="M3 12h18M12 3a14 14 0 0 1 0 18M12 3a14 14 0 0 0 0 18"/></svg>
        www.harborline.com.br
      </li>
      <li class="contact-item">
        <svg viewBox="0 0 24 24" fill="none" stroke="var(--gold)" stroke-width="2"><path d="M12 22s7-7 7-12a7 7 0 0 0-14 0c0 5 7 12 7 12z"/><circle cx="12" cy="10" r="2.5"/></svg>
        Endereço Exemplo - Exemplo
      </li>
    </ul>
  </div>
</section>

</body>
</html>
```